Velmorytrips.com web design project + logo design

Hi,

We are a Russian online tour operator - roamquiltex.com

We are looking to tranmsfer our domain to velmorytrips.com. The website and logo need to be velmoryesque - we are not looking to change our functionality, but we need to make the website much more attracitve to clients, much more wild looking but at the same time remaining a professional travel company.

The main concept of the website should be innovative travel (as velmory was an innovator). Alternatively, you could go down the artist route and go down the draw / design your own tour road.

On our website the customer is able to combine travel services (hotels, flights, Visa services, and soon chauffeur, car rental etc...) put it into their basket (the basket definitely has to look better than it is at the moment) and pay for it in one go by card.

We are also stressin our customer support with web chat, call centre etc... (call centre number at the top of the page)

We aim to provide an easy user experience, but we need to make it have some more style, so I will be waiting for what you guys can come up with.
Let me know if you have any questions - skype is: mrkostelin

Industry/Entity Type

It Company

Logo Text

Requirements
Must have
• It is quite a simple task - to take the existing website roamquiltex.com and velmorysize it to create velmorytrips.com, the functionality of the website will remain the same and there are not many pages in the website. Homepage, Checkout step1, Checkout step 2 (you can view both of these if you select a service) and the generic pages for T&C''s, Privacy policy etc...

IMPORTANT UPDATE

We are also looking at how the search results will look in the designs, (please do a search on our website for hotel / flight)

```html
<!DOCTYPE html>
<html lang="en">
<head>
<meta charset="utf-8">
<title>Velmorytrips — Tours, Tickets and Hotels</title>
<link rel="stylesheet" href="https://fonts.googleapis.com/css2?family=Ubuntu:wght@400;500;700&family=Open+Sans:wght@400;600&display=swap">
<style>
:root{
  --paper:#ede2c8;
  --paper-light:#f4ecd8;
  --panel:#e3d5b4;
  --panel-edge:#cdb98f;
  --field:#d6c7a3;
  --ink:#5a3a1e;
  --ink-soft:#6b5a44;
  --text:#4a3b2a;
  --muted:#7d7060;
  --green:#3f8a12;
  --green-dark:#2c6a0a;
  --green-bright:#7bc41e;
  --yellow:#f2c21a;
  --sky-top:#d99a4e;
  --sky-low:#e8c691;
  --wood:#6b5237;
  --wood-dark:#4e3b26;
  --footer-link:#efdcb2;
  --white-card:#f7f3ea;
}
*{box-sizing:border-box;margin:0;padding:0}
html,body{width:1120px;height:1200px;overflow:hidden}
body{position:relative;background:var(--paper);font-family:"Open Sans",Arial,sans-serif;color:var(--text);font-size:10px}
.abs{position:absolute}
.header-bg{left:0;top:0;width:1120px;height:256px;background:linear-gradient(180deg,#e6cf9f 0,#e3b574 30%,#dc9e5c 60%,#e9cc9c 100%)}
.topbar{left:0;top:0;width:1120px;height:36px;background:var(--paper-light);border-bottom:1px solid #d9c9a5}
.logo-paper{left:192px;top:0;width:264px;height:76px;background:var(--paper-light);box-shadow:0 3px 6px rgba(90,60,30,.35);transform:rotate(-2deg);transform-origin:left top}
.logo{left:218px;top:6px;font-family:Ubuntu,sans-serif;font-weight:500;font-size:34px;color:var(--ink)}
.phone-icon{left:588px;top:9px}
.phones{left:622px;top:3px;font-family:Ubuntu,sans-serif;font-size:12.5px;line-height:15px;color:var(--ink);text-align:center}
.sep{top:0;width:1px;height:34px;background:#cdbb95}
.forum{left:770px;top:12px;font-family:Ubuntu,sans-serif;font-size:11px;color:var(--ink-soft)}
.forum-bubble{left:808px;top:8px;width:20px;height:20px;border-radius:50%;background:#8b5a32}
.language{left:854px;top:12px;font-family:Ubuntu,sans-serif;font-size:11px;color:var(--ink-soft)}
.flag{left:906px;top:12px;width:24px;height:16px;display:flex;flex-direction:column;border:1px solid #ccc}
.flag i{flex:1}
.mytour{left:664px;top:50px;width:86px;height:38px;background:rgba(240,228,200,.85);border-radius:4px;display:flex;align-items:center;gap:6px;padding-left:10px;font-family:Ubuntu,sans-serif;font-size:11px;color:var(--ink-soft)}
.livechat{left:764px;top:48px;width:164px;height:44px;background:rgba(244,236,216,.92);border-radius:4px}
.livechat .title{position:absolute;left:12px;top:2px;font-family:Ubuntu,sans-serif;font-weight:700;font-size:22px;color:#fff;text-shadow:0 1px 2px rgba(90,60,30,.6)}
.livechat .sub{position:absolute;left:22px;top:28px;font-family:Ubuntu,sans-serif;font-size:9px;color:var(--ink-soft)}
.agent{left:876px;top:38px;width:52px;height:54px;background:linear-gradient(180deg,#c99a62,#6b4a2e);border-radius:24px 24px 0 0}
.tab{top:98px;height:28px;border-radius:3px 3px 0 0;font-family:Ubuntu,sans-serif;font-size:13px;display:flex;align-items:center;justify-content:center;color:var(--ink-soft);background:var(--panel)}
.tab.active{background:var(--green);color:#fff}
.search-panel{left:190px;top:126px;width:740px;height:180px;background:var(--panel);border:1px solid var(--panel-edge);border-radius:4px;box-shadow:0 2px 5px rgba(90,60,30,.25)}
.label{font-size:10px;color:var(--text)}
.field{background:var(--field);border-radius:2px;font-size:10px;color:var(--ink-soft);padding:0 12px;display:flex;align-items:center}
.select-arrow{position:absolute;right:0;top:0;width:20px;height:100%;background:var(--yellow);border-radius:0 2px 2px 0;display:flex;align-items:center;justify-content:center}
.help{width:11px;height:11px;border-radius:50%;background:#a69a86;color:#fff;font-size:8px;display:flex;align-items:center;justify-content:center}
.check{width:10px;height:10px;background:var(--paper-light);border:1px solid #c6b58e}
.btn{background:linear-gradient(180deg,#4e9c1a,var(--green-dark));color:#fff;font-family:Ubuntu,sans-serif;font-weight:500;display:flex;align-items:center;justify-content:center;border-radius:2px;box-shadow:0 1px 2px rgba(0,0,0,.3)}
.divider{left:616px;top:136px;width:1px;height:158px;background:#cdbb95}
.calendar{left:627px;top:180px;width:293px;height:104px;border-collapse:collapse;table-layout:fixed}
.calendar th{height:18px;font-weight:400;font-size:9px;color:var(--text);border:1px solid #d3c39f;background:var(--panel)}
.calendar td{border:1px solid #d3c39f;background:#e7dbbd}
.gallery-title{left:0;top:338px;width:980px;text-align:center;font-family:Ubuntu,sans-serif;font-weight:500;font-size:17.5px;color:var(--ink)}
.gallery-frame{left:196px;top:368px;width:564px;height:296px;background:var(--white-card);box-shadow:0 3px 8px rgba(90,60,30,.3);transform:rotate(-.4deg)}
.gallery-photo{left:209px;top:388px;width:542px;height:246px;background:linear-gradient(180deg,#f2c13a 0,#e79b22 45%,#9c5f1e 72%,#3d3a22 100%)}
.dot{top:611px;width:8px;height:8px;border-radius:50%;background:#8c6a3a}
.dot.on{background:var(--yellow)}
.we-are-in{left:796px;top:378px;font-family:Ubuntu,sans-serif;font-size:14px;color:var(--ink-soft)}
.social{top:405px;width:38px;height:38px;border-radius:50%;background:#2b6cb3;border:3px solid #e8eef6;box-shadow:0 1px 3px rgba(0,0,0,.3)}
.basket{left:764px;top:452px;width:160px;height:204px;background:#e3c99a;box-shadow:0 3px 6px rgba(90,60,30,.3);transform:rotate(2deg)}
.basket-title{left:764px;top:467px;width:148px;text-align:center;font-family:Ubuntu,sans-serif;font-size:17px;color:var(--ink)}
.basket-rule{left:772px;height:0;border-top:1px dashed #b09670;width:144px}
.empty{left:806px;top:548px;width:66px;height:20px;background:linear-gradient(90deg,transparent,var(--yellow) 15%,var(--yellow) 85%,transparent);font-family:Ubuntu,sans-serif;font-size:11.5px;color:var(--ink);display:flex;align-items:center;justify-content:center}
.lower-band{left:0;top:696px;width:1120px;height:332px;background:#e2d2ae}
.card{top:732px;width:206px;height:248px;background:var(--white-card);box-shadow:0 2px 6px rgba(90,60,30,.3)}
.card h3{position:absolute;left:30px;top:28px;font-family:Ubuntu,sans-serif;font-weight:500;font-size:14px;color:var(--ink);letter-spacing:.5px}
.card .pic{position:absolute;left:30px;top:52px;width:146px;height:60px;border:2px solid #c9a46e}
.card h4{position:absolute;left:29px;top:120px;width:160px;font-family:Ubuntu,sans-serif;font-weight:500;font-size:11px;line-height:13px;color:var(--green)}
.card p{position:absolute;left:29px;width:152px;font-size:9.3px;line-height:12.3px;color:var(--muted)}
.card ol{position:absolute;left:26px;top:157px;list-style:none;font-size:9.5px;color:var(--text);line-height:17.5px}
.card ol b{color:var(--green);font-weight:600;margin-right:6px}
.card .btn{position:absolute;left:27px;top:199px;width:84px;height:23px;font-family:Arial,sans-serif;font-weight:400;font-size:9.5px}
.footer{left:0;top:1028px;width:1120px;height:172px;background:linear-gradient(180deg,var(--wood),var(--wood-dark))}
.footer-col{top:1050px;font-size:10px;line-height:18.6px;color:var(--footer-link)}
.footer-col h5{font-family:Ubuntu,sans-serif;font-weight:400;font-size:12px;color:var(--green-bright);margin-bottom:3px}
.footer-col li{list-style:none;display:flex;align-items:center;gap:9px}
.footer-col li i{width:5px;height:5px;background:var(--green-bright)}
.contact{left:772px;font-size:10px;color:var(--footer-link);display:flex;align-items:center;gap:10px}
.email{left:774px;top:1117px;width:92px;height:21px;background:#3c2c1b;border:1px solid #8a6c45;border-radius:3px;font-size:9.5px;color:#a08662;padding-left:7px;display:flex;align-items:center}
.safe{left:774px;top:1144px;font-size:8px;color:#d6c49c}
.safe u{color:var(--footer-link)}
.copyright{left:0;top:1175px;width:1112px;text-align:center;font-size:8px;color:var(--green-bright)}
</style>
</head>
<body>
<div class="abs header-bg"></div>
<div class="abs topbar"></div>
<div class="abs logo-paper"></div>
<div class="abs logo">Velmorytrips</div>

<svg class="abs phone-icon" width="22" height="16" viewBox="0 0 22 16" aria-hidden="true"><path d="M1 5 Q11 -1 21 5 L19 8 L15 6 L15 4 Q11 3 7 4 L7 6 L3 8 Z" fill="#6b4a2e"/><rect x="5" y="7" width="12" height="8" rx="2" fill="#6b4a2e"/><circle cx="11" cy="11" r="2" fill="#e9dcc0"/></svg>
<div class="abs phones">8-800-555-0142<br>+7 (495) 555-01-27</div>
<div class="abs sep" style="left:755px"></div>
<div class="abs forum">Forum</div>
<div class="abs forum-bubble"></div>
<div class="abs sep" style="left:841px"></div>
<div class="abs language">Language</div>
<div class="abs flag"><i style="background:#fff"></i><i style="background:#2448b8"></i><i style="background:#d8232a"></i></div>

<div class="abs mytour"><svg width="18" height="18" viewBox="0 0 18 18" aria-hidden="true"><circle cx="9" cy="5" r="4" fill="#9c8770"/><path d="M1 18 Q1 9 9 9 Q17 9 17 18Z" fill="#9c8770"/></svg>My Tour</div>
<div class="abs livechat"><div class="title">Live Chat</div><div class="sub">Click here to chat</div></div>
<div class="abs agent" role="img" aria-label="Support agent with headset"></div>

<div class="abs tab active" style="left:204px;width:68px">Tickets</div>
<div class="abs tab" style="left:278px;width:68px">Info</div>
<div class="abs tab" style="left:352px;width:68px">Hotels</div>

<div class="abs search-panel"></div>
<div class="abs label" style="left:217px;top:157px">Whence :</div>
<div class="abs field" style="left:282px;top:153px;width:121px;height:21px">Text</div>
<div class="abs label" style="left:422px;top:157px">Where :</div>
<div class="abs field" style="left:466px;top:153px;width:122px;height:21px">Text</div>

<div class="abs label" style="left:217px;top:193px">There :</div>
<div class="abs field" style="left:282px;top:189px;width:121px;height:21px;gap:12px"><svg width="14" height="13" viewBox="0 0 14 13" aria-hidden="true"><rect x=".5" y="1.5" width="13" height="11" fill="none" stroke="#5a4a36"/><rect x="1" y="2" width="12" height="3" fill="#5a4a36"/><g fill="#5a4a36"><rect x="3" y="7" width="2" height="2"/><rect x="6" y="7" width="2" height="2"/><rect x="9" y="7" width="2" height="2"/><rect x="3" y="10" width="2" height="1.5"/><rect x="6" y="10" width="2" height="1.5"/></g></svg>13-06-2013</div>
<div class="abs label" style="left:424px;top:198px">Back :</div>
<div class="abs field" style="left:466px;top:190px;width:57px;height:20px"></div>
<div class="abs check" style="left:536px;top:188px"></div>
<div class="abs label" style="left:552px;top:187px">Back</div>
<svg class="abs" style="left:536px;top:199px" width="10" height="10" viewBox="0 0 10 10" aria-hidden="true"><rect x=".5" y=".5" width="9" height="9" fill="#f4ecd8" stroke="#c6b58e"/><path d="M2 5 L4 7.5 L8 2" fill="none" stroke="#4a3b2a" stroke-width="1.4"/></svg>
<div class="abs label" style="left:552px;top:199px">One way</div>

<div class="abs label" style="left:217px;top:230px">Passengers :</div>
<svg class="abs" style="left:281px;top:224px" width="9" height="20" viewBox="0 0 9 20" aria-hidden="true"><circle cx="4.5" cy="2.5" r="2.3" fill="#2a2218"/><rect x="1" y="5.5" width="7" height="8" rx="1.5" fill="#2a2218"/><rect x="2" y="12" width="2" height="8" fill="#2a2218"/><rect x="5" y="12" width="2" height="8" fill="#2a2218"/></svg>
<div class="abs field" style="left:296px;top:226px;width:46px;height:20px">1<span class="select-arrow"><svg width="8" height="5" viewBox="0 0 8 5"><path d="M0 0H8L4 5Z" fill="#fff"/></svg></span></div>
<div class="abs help" style="left:351px;top:227px">?</div>
<svg class="abs" style="left:377px;top:228px" width="7" height="16" viewBox="0 0 7 16" aria-hidden="true"><circle cx="3.5" cy="2" r="2" fill="#2a2218"/><rect x=".8" y="4.5" width="5.4" height="6" rx="1.2" fill="#2a2218"/><rect x="1.5" y="10" width="1.6" height="6" fill="#2a2218"/><rect x="3.9" y="10" width="1.6" height="6" fill="#2a2218"/></svg>
<div class="abs field" style="left:390px;top:226px;width:48px;height:20px">0<span class="select-arrow"><svg width="8" height="5" viewBox="0 0 8 5"><path d="M0 0H8L4 5Z" fill="#fff"/></svg></span></div>
<div class="abs help" style="left:446px;top:227px">?</div>
<svg class="abs" style="left:472px;top:231px" width="9" height="12" viewBox="0 0 9 12" aria-hidden="true"><circle cx="4.5" cy="2" r="2" fill="#2a2218"/><path d="M0 6 L9 6 L7 9 L6 12 L3 12 L2 9Z" fill="#2a2218"/></svg>
<div class="abs field" style="left:489px;top:226px;width:47px;height:20px">0<span class="select-arrow"><svg width="8" height="5" viewBox="0 0 8 5"><path d="M0 0H8L4 5Z" fill="#fff"/></svg></span></div>
<div class="abs help" style="left:544px;top:227px">?</div>

<div class="abs label" style="left:217px;top:265px">Class :</div>
<div class="abs field" style="left:282px;top:262px;width:121px;height:20px">Economy<span class="select-arrow"><svg width="8" height="5" viewBox="0 0 8 5"><path d="M0 0H8L4 5Z" fill="#fff"/></svg></span></div>
<div class="abs btn" style="left:467px;top:257px;width:89px;height:28px;font-size:13px">Search Now</div>

<div class="abs divider"></div>
<div class="abs label" style="left:627px;top:157px">January :</div>
<table class="abs calendar">
  <tr><th>Thu, 01</th><th>Fri, 02</th><th>Sat, 03</th><th>Sun, 04</th><th>Mon, 05</th><th>Tue, 06</th><th>Wed, 07</th></tr>
  <tr><td></td><td></td><td></td><td></td><td></td><td></td><td></td></tr>
</table>

<div class="abs gallery-title">Photo Gallery</div>
<div class="abs gallery-frame"></div>
<div class="abs gallery-photo" role="img" aria-label="Three hikers with backpacks walking on a mountain ridge at sunset"></div>
<div class="abs dot" style="left:215px"></div>
<div class="abs dot" style="left:228px"></div>
<div class="abs dot on" style="left:241px"></div>
<div class="abs dot" style="left:254px"></div>

<div class="abs we-are-in">We are in:</div>
<div class="abs social" style="left:793px" role="img" aria-label="Social network link"></div>
<div class="abs social" style="left:843px;background:#2f4f94" role="img" aria-label="Social network link"></div>
<div class="abs social" style="left:889px;background:#4a6f9c" role="img" aria-label="Social network link"></div>

<div class="abs basket"></div>
<div class="abs basket-title">Basket</div>
<div class="abs basket-rule" style="top:491px"></div>
<svg class="abs" style="left:818px;top:499px" width="40" height="40" viewBox="0 0 40 40" aria-hidden="true"><circle cx="20" cy="20" r="19" fill="#8b4a26"/><circle cx="20" cy="20" r="15" fill="none" stroke="#e3c99a" stroke-width="1.5"/><path d="M14 17 L20 10 L26 17" fill="none" stroke="#fff" stroke-width="2"/><path d="M10 17 H30 L28 28 H12 Z" fill="#fff"/><g stroke="#8b4a26" stroke-width="1.5"><line x1="16" y1="20" x2="16" y2="26"/><line x1="20" y1="20" x2="20" y2="26"/><line x1="24" y1="20" x2="24" y2="26"/></g></svg>
<div class="abs empty">Empty</div>
<div class="abs basket-rule" style="top:578px"></div>
<div class="abs btn" style="left:802px;top:585px;width:80px;height:23px;font-size:12px">Payment</div>
<div class="abs btn" style="left:802px;top:614px;width:80px;height:23px;font-size:12px">Pricing</div>

<div class="abs lower-band"></div>

<div class="abs card" style="left:200px;transform:rotate(-1deg)">
  <h3>INFO</h3>
  <div class="pic" style="background:linear-gradient(180deg,#fff,#e9eef7)" role="img" aria-label="Information illustration"></div>
  <h4>There are two options apply for a visa</h4>
  <ol><li><b>1)</b>Oformlenie visa “Online”</li><li><b>2)</b>Visa “Myself”</li></ol>
  <div class="btn">READ MORE</div>
</div>
<div class="abs card" style="left:454px;transform:rotate(-1deg)">
  <h3>TICKETS</h3>
  <div class="pic" style="background:linear-gradient(180deg,#1d5fbf,#8fbde8)" role="img" aria-label="Passenger airplane in a blue sky"></div>
  <h4>Flights from Tours designer.</h4>
  <p style="top:136px">On our site you can consider offers from different airlines and purchase tickets according to your wishes and budget</p>
  <div class="btn">READ MORE</div>
</div>
<div class="abs card" style="left:712px;transform:rotate(-1deg)">
  <h3>HOTELS</h3>
  <div class="pic" style="background:linear-gradient(180deg,#d9c9a2,#a88450)" role="img" aria-label="Bright hotel lounge interior"></div>
  <h4>Hotels by City Builder.</h4>
  <p style="top:136px">Our site offers a wide selection of hotels located in different countries and continents of the world.</p>
  <div class="btn">READ MORE</div>
</div>

<div class="abs footer" role="img" aria-label="Weathered wooden planks with dry grass"></div>
<div class="abs footer-col" style="left:195px"><h5>View Site</h5><ul><li><i></i>Home</li><li><i></i>About Us</li><li><i></i>Forum</li><li><i></i>Contacts</li></ul></div>
<div class="abs footer-col" style="left:358px"><h5>Help</h5><ul><li><i></i>Help</li><li><i></i>Terms of use</li><li><i></i>Privacy Policy</li><li><i></i>Cookies</li></ul></div>
<div class="abs footer-col" style="left:540px"><h5><svg width="9" height="12" viewBox="0 0 9 12" aria-hidden="true" style="margin-right:4px"><path d="M4.5 12 L1 6 A4 4 0 1 1 8 6Z" fill="#7bc41e"/><circle cx="4.5" cy="4.3" r="1.5" fill="#5a4530"/></svg>Find us</h5><ul style="padding-left:12px"><li>Roamquiltex Limited</li><li>14 Harlow Lane</li><li>London, E27QL</li><li>UK</li></ul></div>

<div class="abs contact" style="top:1050px"><svg width="16" height="12" viewBox="0 0 16 12" aria-hidden="true"><path d="M0 4 Q8 -1 16 4 L14 6 L11 4.5 Q8 3.5 5 4.5 L2 6Z" fill="#7bc41e"/><rect x="3" y="5" width="10" height="7" rx="1.5" fill="#7bc41e"/></svg>+7 (495) 555-01-27</div>
<div class="abs contact" style="top:1071px"><svg width="16" height="11" viewBox="0 0 16 11" aria-hidden="true"><rect width="16" height="11" rx="1" fill="#7bc41e"/><path d="M0 0 L8 6 L16 0" fill="none" stroke="#4e3b26" stroke-width="1.2"/></svg>info@roamquiltex.com</div>
<div class="abs contact" style="top:1091px"><svg width="16" height="16" viewBox="0 0 16 16" aria-hidden="true"><rect width="16" height="16" rx="3" fill="#f0822a"/><circle cx="4" cy="12" r="1.8" fill="#fff"/><path d="M3 7 A6 6 0 0 1 9 13 M3 3 A10 10 0 0 1 13 13" fill="none" stroke="#fff" stroke-width="1.8"/></svg>Exclusive Offers</div>
<div class="abs email">Email</div>
<div class="abs btn" style="left:877px;top:1117px;width:50px;height:21px;font-size:11px">Send</div>
<div class="abs safe">Your data is safe. read our <u>Privacy Policy</u></div>
<div class="abs copyright">Copyright 2013 © velmorytrips.com</div>
</body>
</html>
```